Design for Broadband Data Consumption Calculator

Primary Inspiration: http://www.quorvantel.example/b2c/splash/datacalculatorPopup.jsp
This is the functionality we are looking for, but we want to use the design colors from our current site on NetkiggerTorvet.dk
Secondary Inspiration: http://www.7.example/Privat/Mobil/Databeregner/#dc
Description
This will be a list of questions (three part, where the third part is the presentation of the price chart) that will enable us to present a list of mobile broadband providers that is suited for their needs.
Mock Up provided as well as thorough project description
Look and feel
Each slider illustrates characteristics of the customer's brand and the style your logo design should communicate.

```html
<!DOCTYPE html>
<html lang="en">
<head>
<meta charset="utf-8">
<title>Netkiggertorvet – Mobile Broadband Calculator</title>
<link href="https://fonts.googleapis.com/css2?family=Ubuntu:wght@400;500;700&family=Arimo:wght@400;700&display=swap" rel="stylesheet">
<style>
:root{
  --teal:#2bb3ad;
  --blue:#1a9fd8;
  --blue-dark:#0f6f99;
  --ink:#222;
  --grey-text:#8a8a8a;
  --panel-border:#d6d6d6;
  --row-alt:#ececec;
  --track:#d9d9d9;
  --track-inner:#8f8f8f;
  --green:#8cc21f;
  --green-dark:#6d9c12;
  --sky:#2a7f9c;
  --cloud:#e9e9e9;
}
*{box-sizing:border-box;margin:0;padding:0}
html,body{width:934px;height:1200px;overflow:hidden;background:#fff}
body{font-family:"Arimo",Arial,sans-serif;color:var(--ink)}
.page{position:absolute;left:0;top:0;width:900px;height:1156px;transform:scale(1.03778);transform-origin:0 0}
.abs{position:absolute}

/* header */
.header-band{left:0;top:0;width:900px;height:47px;background:linear-gradient(#3cc2bb,var(--teal))}
.brand{left:150px;top:20px;font-family:"Ubuntu",sans-serif;font-weight:500;font-size:16px;color:#fff;display:flex;align-items:center;gap:5px;white-space:nowrap}
.brand-dot{width:9px;height:9px;border-radius:50%;background:#fff}
.tagline{left:297px;top:6px;width:318px;height:18px;background:#fff;font-size:9px;line-height:18px;text-align:center;white-space:nowrap}
.why-box{left:623px;top:6px;width:120px;height:27px;background:#fff;font-size:8px;font-weight:700;line-height:9px;padding:4px 0 0 22px}
.why-box::before{content:"?";position:absolute;left:6px;top:2px;font-size:20px;color:#ddd}
.nav{left:146px;top:47px;width:596px;height:25px;background:#fff;display:flex;align-items:center;font-family:"Ubuntu",sans-serif;font-size:11.5px;white-space:nowrap;overflow:hidden}
.nav a{color:var(--ink);text-decoration:none;padding:0 6px;height:25px;line-height:25px;white-space:nowrap;display:flex;align-items:center}
.nav a.active{background:linear-gradient(#4ab6e6,var(--blue));color:#fff;padding:0 9px;border-top:3px solid #0e6f9a;line-height:22px;height:25px}
.nav .caret{font-size:7px;margin-left:2px}
.nav .info{display:inline-block;width:12px;height:12px;border-radius:50%;background:#222;color:#fff;font-size:9px;text-align:center;line-height:12px;margin-right:4px;font-weight:700}
.search{margin-left:auto;display:flex;margin-right:3px;flex:none}
.search span{width:106px;height:18px;border:1px solid #aaa;font-size:8.5px;line-height:16px;padding-left:4px;font-family:"Arimo",sans-serif}
.search b{width:24px;height:18px;background:#222;display:block;position:relative}
.search b svg{position:absolute;left:6px;top:3px}

/* panels */
.panel{left:146px;width:599px;background:linear-gradient(#f2f2f2,#fff 40%);border:1px solid var(--panel-border)}
.panel-title{font-family:"Ubuntu",sans-serif;font-weight:500;font-size:14px;color:#666;white-space:nowrap}
.panel-title em{font-style:normal;color:var(--blue)}
.icon-circle{width:20px;height:20px;border-radius:50%}

/* device */
.device-panel{top:84px;height:67px;background:#fff}
.device-q{left:14px;top:14px;font-family:"Ubuntu",sans-serif;font-weight:500;font-size:13.5px;line-height:19px}
.device-q em{font-style:normal;color:var(--blue)}
.device-bar{left:205px;top:0;width:393px;height:65px;background:#f1f1f1;border-left:1px solid #ddd}
.device{top:7px;height:52px;width:78px;background:#e3e3e3;border:1px solid #d0d0d0;font-size:7.5px;font-weight:700;text-align:center}
.device.selected{background:var(--blue);color:#fff;border-color:var(--blue-dark)}
.device .check{position:absolute;right:8px;top:8px;width:12px;height:12px;background:#c9c9c9;border:1px solid #aaa}
.device.selected .check{background:#fff}
.device .label{position:absolute;right:3px;top:26px;width:38px;line-height:10px}
.device-photo{border-radius:3px}

/* sliders */
.slider{width:278px;height:18px;border-radius:9px;background:var(--track);box-shadow:inset 0 1px 2px rgba(0,0,0,.15)}
.slider .groove{position:absolute;left:7px;top:5px;right:7px;height:7px;border-radius:4px;background:var(--track-inner)}
.slider .fill{position:absolute;left:7px;top:5px;height:7px;border-radius:4px;background:linear-gradient(#3bb2e4,var(--blue-dark))}
.slider .knob{position:absolute;top:3px;width:11px;height:11px;border-radius:50%;background:radial-gradient(#fff,#9a9a9a);border:1px solid #777;margin-left:-5px}
.ticks{width:278px;height:10px;font-size:7.5px;color:var(--grey-text);font-weight:700}
.ticks span{position:absolute;transform:translateX(-50%);white-space:nowrap}
.ticks span.on{color:var(--ink)}
.q-label{font-size:8.5px;font-weight:700;white-space:nowrap}
.q-label small{font-size:8.5px;color:var(--grey-text);font-weight:700}
.row-alt{left:4px;width:590px;height:80px;background:var(--row-alt)}

/* essentials */
.big-slider{left:10px;top:48px;width:578px;height:18px}
.tick-line{top:64px;width:1px;height:6px;background:#bbb}
.ess-label{top:77px;font-size:8px;color:var(--grey-text);font-weight:700;text-align:center;width:110px;line-height:11px;transform:translateX(-50%)}
.ess-label.on{color:var(--ink)}

.compare-tab{left:752px;top:357px;width:131px;height:33px;background:var(--green);border-radius:4px 0 0 4px;color:#fff;text-align:center;font-weight:700;font-size:11px;padding-top:5px;line-height:12px;white-space:nowrap}
.compare-tab small{font-size:7px;font-weight:400}
.compare-tab b{font-weight:700}
.compare-tab::before{content:"";position:absolute;left:-6px;top:11px;border:6px solid transparent;border-left:0;border-right-color:var(--green)}

.consumption-title{left:0;width:900px;top:756px;text-align:center;font-family:"Ubuntu",sans-serif;font-weight:500;font-size:13.5px;color:var(--blue)}
.gb-bubble{left:360px;top:792px;width:50px;height:20px;background:#d6d6d6;border-radius:3px;font-size:12px;text-align:center;line-height:20px;font-family:"Ubuntu",sans-serif}
.gb-bubble::after{content:"";position:absolute;left:21px;bottom:-5px;border:4px solid transparent;border-top-color:#d6d6d6;border-bottom:0}
.compare-btn{left:604px;top:862px;width:130px;height:29px;border-radius:8px;background:linear-gradient(#9ed23a,var(--green-dark));color:#fff;font-weight:700;font-size:11px;text-align:center;line-height:29px;box-shadow:0 1px 2px rgba(0,0,0,.3)}

/* footer */
.skyline{left:0;top:915px;width:900px;height:241px;background:linear-gradient(#fff 0%,#eef3f5 18%,#8fbccb 38%,#dfe6e8 55%,var(--cloud) 100%)}
.footer-box{left:150px;top:1008px;width:589px;height:132px;background:#dedede;border:1px solid #c4c4c4;box-shadow:0 2px 4px rgba(0,0,0,.2)}
.footer-col{top:0;width:170px}
.footer-col h3{font-family:"Ubuntu",sans-serif;font-weight:700;font-size:13px;text-align:center;padding-top:8px;height:36px;white-space:nowrap}
.footer-col p,.footer-col li{font-size:6.5px;line-height:8px}
.footer-col ul{list-style:none}
.footer-col li{margin-bottom:5px;padding-left:8px;position:relative}
.footer-col li::before{content:"›";position:absolute;left:0}
</style>
</head>
<body>
<div class="page">

  <header>
    <div class="abs header-band"></div>
    <div class="abs brand"><span class="brand-dot"></span>Netkiggertorvet</div>
    <div class="abs tagline">Aktuelle prisoversigter og gratis hjælp, når du skal finde nyt bredbånd</div>
    <div class="abs why-box">Hvorfor skal jeg bruge netkiggertorvet?</div>
    <nav class="abs nav">
      <a class="active">Forsiden</a>
      <a>Prisoversigter<span class="caret">▾</span></a>
      <a>Anmeldelser<span class="caret">▾</span></a>
      <a>Artikler</a>
      <a>Hastighedsguide</a>
      <a><span class="info">i</span>Om Os</a>
      <div class="search"><span>Søgefelt...</span><b><svg width="12" height="12" viewBox="0 0 12 12"><circle cx="5" cy="5" r="3.5" fill="none" stroke="#fff" stroke-width="1.6"/><line x1="7.5" y1="7.5" x2="11" y2="11" stroke="#fff" stroke-width="1.8"/></svg></b></div>
    </nav>
  </header>

  <section class="abs panel device-panel">
    <div class="abs device-q">What <em>device</em> do you need<br><em>mobile broadband</em> for?</div>
    <div class="abs device-bar">
      <div class="abs device" style="left:22px"><div class="abs device-photo" role="img" aria-label="Smartphone" style="left:6px;top:4px;width:20px;height:44px;background:linear-gradient(#555,#111)"></div><span class="check"></span><span class="label">Smart Phone</span></div>
      <div class="abs device selected" style="left:115px"><div class="abs device-photo" role="img" aria-label="Tablet" style="left:-8px;top:-6px;width:42px;height:60px;background:linear-gradient(#4a4a4a,#111)"></div><span class="check"><svg width="10" height="10" viewBox="0 0 10 10"><path d="M1 5l3 3 5-7" fill="none" stroke="#1a9fd8" stroke-width="1.6"/></svg></span><span class="label">Tablet</span></div>
      <div class="abs device" style="left:208px"><div class="abs device-photo" role="img" aria-label="Desktop PC tower" style="left:-6px;top:-4px;width:34px;height:56px;background:linear-gradient(90deg,#ccc,#eee,#aaa)"></div><span class="check"></span><span class="label">PC With router</span></div>
      <div class="abs device" style="left:301px"><div class="abs device-photo" role="img" aria-label="Laptop" style="left:-14px;top:14px;width:46px;height:34px;background:linear-gradient(#8a6bb0,#c9c9c9)"></div><span class="check"></span><span class="label">PC With broadband</span></div>
    </div>
  </section>

  <section class="abs panel" style="top:164px;height:117px">
    <div class="abs icon-circle" style="left:14px;top:12px;background:radial-gradient(#fff 30%,#e2572b 35%,#333 80%)"></div>
    <div class="abs panel-title" style="left:45px;top:15px">Essentials: <em>How often are you online?</em></div>
    <div class="abs big-slider slider"><span class="groove"></span><span class="fill" style="width:210px"></span><span class="knob" style="left:217px"></span></div>
    <div class="abs tick-line" style="left:77px"></div><div class="abs tick-line" style="left:228px"></div><div class="abs tick-line" style="left:377px"></div><div class="abs tick-line" style="left:527px"></div>
    <div class="abs ess-label" style="left:77px">A couple of times<br>a week or less..</div>
    <div class="abs ess-label on" style="left:228px">Every day..</div>
    <div class="abs ess-label" style="left:377px">Multiple times<br>a day</div>
    <div class="abs ess-label" style="left:527px">Online all day</div>
  </section>

  <section class="abs panel" style="top:297px;height:442px">
    <div class="abs icon-circle" style="left:14px;top:13px;background:radial-gradient(#fff 20%,#2a86c8 60%,#174d7a)"></div>
    <div class="abs panel-title" style="left:45px;top:15px">Details: <em>What are you going to use your mobile broadband for?</em></div>
    <div class="abs row-alt" style="top:118px"></div>
    <div class="abs row-alt" style="top:280px"></div>

    <div class="abs q-label" style="left:29px;top:52px">Surfing, reading articles, netbanking</div>
    <div class="abs slider" style="left:9px;top:68px"><span class="groove"></span><span class="fill" style="width:23px"></span><span class="knob" style="left:30px"></span></div>
    <div class="abs ticks" style="left:9px;top:91px"><span class="on" style="left:30px">Never</span><span style="left:139px">Sometimes</span><span style="left:247px">Often</span></div>
    <div class="abs q-label" style="left:329px;top:52px">Sending e-mails <small>(with photos)</small></div>
    <div class="abs slider" style="left:309px;top:68px"><span class="groove"></span><span class="fill" style="width:240px"></span><span class="knob" style="left:247px"></span></div>
    <div class="abs ticks" style="left:309px;top:91px"><span style="left:30px">Never</span><span style="left:139px">Sometimes</span><span class="on" style="left:247px">Often</span></div>

    <div class="abs q-label" style="left:29px;top:133px">Social media <small>(Chirpbook, Flitter, etc.)</small></div>
    <div class="abs slider" style="left:9px;top:149px"><span class="groove"></span><span class="fill" style="width:240px"></span><span class="knob" style="left:247px"></span></div>
    <div class="abs ticks" style="left:9px;top:172px"><span style="left:30px">Never</span><span style="left:139px">Sometimes</span><span class="on" style="left:247px">Often</span></div>
    <div class="abs q-label" style="left:329px;top:133px">Sending e-mails <small>(without photos)</small></div>
    <div class="abs slider" style="left:309px;top:149px"><span class="groove"></span><span class="fill" style="width:132px"></span><span class="knob" style="left:139px"></span></div>
    <div class="abs ticks" style="left:309px;top:172px"><span style="left:30px">Never</span><span class="on" style="left:139px">Sometimes</span><span style="left:247px">Often</span></div>

    <div class="abs q-label" style="left:29px;top:214px">Watching videos online <small>(Vidtube, TV7.example, etc.)</small></div>
    <div class="abs slider" style="left:9px;top:230px"><span class="groove"></span><span class="fill" style="width:240px"></span><span class="knob" style="left:247px"></span></div>
    <div class="abs ticks" style="left:9px;top:253px"><span style="left:30px">Never</span><span style="left:139px">Sometimes</span><span class="on" style="left:247px">Often</span></div>
    <div class="abs q-label" style="left:329px;top:214px">Listening to music online</div>
    <div class="abs slider" style="left:309px;top:230px"><span class="groove"></span><span class="fill" style="width:23px"></span><span class="knob" style="left:30px"></span></div>
    <div class="abs ticks" style="left:309px;top:253px"><span class="on" style="left:30px">Never</span><span style="left:139px">Sometimes</span><span style="left:247px">Often</span></div>

    <div class="abs q-label" style="left:29px;top:295px">Download smaller files <small>(below 50 megabytes)</small></div>
    <div class="abs slider" style="left:9px;top:311px"><span class="groove"></span><span class="fill" style="width:23px"></span><span class="knob" style="left:30px"></span></div>
    <div class="abs ticks" style="left:9px;top:334px"><span class="on" style="left:30px">Never</span><span style="left:139px">Sometimes</span><span style="left:247px">Often</span></div>
    <div class="abs q-label" style="left:329px;top:295px">Play online video games</div>
    <div class="abs slider" style="left:309px;top:311px"><span class="groove"></span><span class="fill" style="width:132px"></span><span class="knob" style="left:139px"></span></div>
    <div class="abs ticks" style="left:309px;top:334px"><span style="left:30px">Never</span><span class="on" style="left:139px">Sometimes</span><span style="left:247px">Often</span></div>

    <div class="abs q-label" style="left:29px;top:376px">Download medium files <small>(50-100 megabytes)</small></div>
    <div class="abs slider" style="left:9px;top:392px"><span class="groove"></span><span class="fill" style="width:240px"></span><span class="knob" style="left:247px"></span></div>
    <div class="abs ticks" style="left:9px;top:415px"><span style="left:30px">Never</span><span style="left:139px">Sometimes</span><span class="on" style="left:247px">Often</span></div>
    <div class="abs q-label" style="left:329px;top:376px">Download large files <small>(over 100 megabytes)</small></div>
    <div class="abs slider" style="left:309px;top:392px"><span class="groove"></span><span class="fill" style="width:132px"></span><span class="knob" style="left:139px"></span></div>
    <div class="abs ticks" style="left:309px;top:415px"><span style="left:30px">Never</span><span class="on" style="left:139px">Sometimes</span><span style="left:247px">Often</span></div>
  </section>

  <div class="abs compare-tab">Compare prices for<br><small><b>15GB</b> data mobile broadband</small></div>

  <h2 class="abs consumption-title">Your estimated consumption</h2>
  <div class="abs gb-bubble">15GB</div>
  <div class="abs slider" style="left:156px;top:817px;width:578px;height:16px"><span class="groove" style="top:4px"></span><span class="fill" style="width:222px;top:4px"></span><span class="knob" style="left:229px;top:2px"></span></div>
  <div class="abs compare-btn">Compare prices &nbsp;»</div>

  <footer>
    <div class="abs skyline" role="img" aria-label="City skyline silhouette rising above soft clouds"></div>
    <div class="abs footer-box">
      <div class="abs footer-col" style="left:30px">
        <h3>Om Netkiggertorvet</h3>
        <p style="padding-left:14px"><b>NetkiggerTorvet.dk</b> drives af:<br>Torvholm ApS<br>Kildevej 4B<br>8800 Vestby<br><br>CVR: 40112233<br>Tlf.: 40 12 34 56</p>
      </div>
      <div class="abs footer-col" style="left:215px">
        <h3>Sidste Kommentarer</h3>
        <ul><li>Hej Peter, De skal ikke betale. Der e ...</li><li>Hej igen Nu har jeg fået installeret 3 ...</li><li>Hej Trine, Hvis du oplyser hvilken by d ...</li><li>Hej Jeg bor også på landet og kan se ...</li><li>Hej Gitte, Det billigste jeg kunne find ...</li></ul>
      </div>
      <div class="abs footer-col" style="left:398px">
        <h3>Seneste Nyheder</h3>
        <ul><li>Hvad er det bedste Horizonnet alternativ?</li><li>Hjælp til kunder efter Horizonnet konkurs</li><li>Hvilke kendetegn har de gode internet udbydere til fælles?</li><li>Skjulte faktorer du sikkert ikke måler billig internet på</li><li>Sådan finder du ud af om billig bredbånd er for dig</li></ul>
      </div>
    </div>
  </footer>

</div>
</body>
</html>
```